Reaching the Root: Reason in Clinical Choice-Making

I'd like a cover that looks like it would fit on the shelf next to "The Illness Illusion" by Conrad Meltby, "The Close of Forgetting" by Hugh Falkner, "Meal Mend" by Paul Ostrick, "The Energy Restart Plan" by Victor Pemberly or "The Gland Restart Plan" by the same or "The Cortex Restart Plan" by the same ... either text only (with some interesting fonts that make the title stand out, and the subtitle smaller) or a relevant image, though I'm not entirely sure what that would be since this is a book about big-picture medical decision making.
Author name is Dr Miriam Calloway, NMD
I'll eventually request an e-book, paperback, and audio cover from the winner...

Target Market(s)

practicing physicians

Industry/Entity Type

medicine

Requirements
Must have
• look similar to other books in the genre

```html
<!DOCTYPE html>
<html lang="en">
<head>
<meta charset="utf-8">
<title>Reaching the Root: Reason in Clinical Choice-Making</title>
<link rel="stylesheet" href="https://fonts.googleapis.com/css2?family=Bebas+Neue&family=Courier+Prime:wght@700&family=Work+Sans:wght@400&display=swap">
<style>
  :root {
    --cover-grey: #bdb9b5;
    --edge-light: #e8e6e2;
    --edge-dark: #a9a5a1;
    --ink: #0d0d0d;
    --root-red: #c03a31;
    --paper-white: #ffffff;
    --maze-tone: #5a5856;
  }
  html, body {
    margin: 0;
    padding: 0;
    width: 800px;
    height: 1200px;
    overflow: hidden;
  }
  .cover {
    position: relative;
    width: 800px;
    height: 1200px;
    background: linear-gradient(to right,
      var(--edge-light) 0px,
      var(--edge-dark) 30px,
      var(--cover-grey) 160px,
      var(--cover-grey) 640px,
      #c6c3bf 720px,
      var(--edge-light) 800px);
  }
  .cover-art {
    position: absolute;
    inset: 0;
    width: 800px;
    height: 1200px;
  }
  .title-main,
  .title-small {
    font-family: "Courier Prime", "Courier New", monospace;
    font-weight: 700;
    fill: var(--ink);
  }
  .title-main { font-size: 190px; }
  .title-small { font-size: 118px; }
  .title-hero {
    font-family: "Bebas Neue", "Oswald", sans-serif;
    font-size: 620px;
    fill: var(--root-red);
  }
  .subtitle {
    font-family: "Courier Prime", "Courier New", monospace;
    font-weight: 700;
    font-size: 44px;
    fill: var(--paper-white);
  }
  .maze-mark { fill: var(--maze-tone); }
  .author {
    font-family: "Work Sans", "Helvetica", sans-serif;
    font-weight: 400;
    font-size: 46px;
    fill: var(--ink);
  }
</style>
</head>
<body>
  <main class="cover">
    <svg class="cover-art" viewBox="0 0 800 1200" xmlns="http://www.w3.org/2000/svg">
      <g class="title">
        <text class="title-main" x="71" y="250" textLength="674" lengthAdjust="spacingAndGlyphs">Reaching</text>
        <text class="title-small" x="62" y="381" textLength="132" lengthAdjust="spacingAndGlyphs">the</text>
        <text class="title-hero" x="204" y="745" textLength="531" lengthAdjust="spacingAndGlyphs">ROOT</text>
      </g>

      <rect class="maze-mark" x="235" y="785" width="193" height="85" role="img" aria-label="Square maze graphic in black line work"/>

      <g class="subtitle-block">
        <text class="subtitle" x="453" y="815" textLength="223" lengthAdjust="spacingAndGlyphs">REASON IN</text>
        <text class="subtitle" x="453" y="872" textLength="223" lengthAdjust="spacingAndGlyphs">CLINICAL</text>
        <text class="subtitle" x="237" y="928" textLength="439" lengthAdjust="spacingAndGlyphs">CHOICE-MAKING</text>
      </g>

      <text class="author" x="137" y="1144" textLength="526" lengthAdjust="spacingAndGlyphs">DR MIRIAM CALLOWAY, NMD</text>
    </svg>
  </main>
</body>
</html>
```